Visitenkarten-Design für freie Trauerrednerin
Viele Ideen, viele Vorschläge, orientiert sich an den Kundenwünschen, nimmt immer wieder Anpassungen vor, gute Kommunikation während des Projekts. Ich bin sehr zufrieden.
Zielgruppe
Ich bin Freie Trauerrednerin, also in selbständiger Tätigkeit. (Damit ist auch die Zielgruppe erklärt)
Aufgabenstellung
Das Anliegen sollte erkennbar sein und ein Foto (Naturfotografie) passender Natur sollte den ganzen Hintergrund ausfüllen. Kontaktdaten sollten wie folgt erscheinen: Name, Vorname, Telefon, E-Mail-Adresse, Anschrift mit PLZ, Ort, Straße, Hausnummer.
Auf der Vorderseite sollte nur mein Name und meine Tätigkeit stehen, auf der Rückseite nochmals Name und Tätigkeit und alle restlichen Daten.
Die hochgeladene Datei ist ein Beispiel meiner engeren Vorstellung des Designs.

```html
<!DOCTYPE html>
<html lang="de">
<head>
<meta charset="utf-8">
<title>Visitenkarte Trauerrednerin</title>
<link rel="stylesheet" href="https://fonts.googleapis.com/css2?family=Mrs+Saint+Delafield&family=Mulish:wght@500;600;700&display=swap">
<style>
  :root {
    --page-bg: #ededed;
    --card-dark: #0e0f11;
    --fern-deep: #123a26;
    --fern-mid: #1d5a37;
    --card-light: #ffffff;
    --pattern-tint: #dde8e3;
    --pattern-soft: #f2f6f4;
    --ink: #111111;
    --paper-text: #ffffff;
    --sage: #5b8a74;
  }
  * { margin: 0; padding: 0; box-sizing: border-box; }
  html, body {
    width: 1200px;
    height: 858px;
    overflow: hidden;
    background: var(--page-bg);
  }
  .sheet {
    position: relative;
    width: 1200px;
    height: 858px;
  }
  .card {
    position: absolute;
    top: 272px;
    width: 486px;
    height: 314px;
    overflow: hidden;
  }
  .card--front { left: 83px; background: var(--card-dark); }
  .card--back  { left: 630px; background: var(--card-light); }

  .card__photo {
    position: absolute;
    inset: 0;
    background:
      radial-gradient(ellipse 55% 45% at 38% 28%, var(--fern-mid) 0%, rgba(29,90,55,0.35) 55%, transparent 80%),
      radial-gradient(ellipse 40% 35% at 70% 60%, var(--fern-deep) 0%, transparent 75%),
      radial-gradient(ellipse 45% 40% at 25% 85%, rgba(18,58,38,0.7) 0%, transparent 80%),
      var(--card-dark);
  }
  .card__pattern {
    position: absolute;
    inset: 0;
    background: linear-gradient(135deg, var(--pattern-tint) 0%, var(--pattern-soft) 50%, var(--pattern-tint) 100%);
  }

  .identity {
    position: absolute;
    right: 48px;
    text-align: right;
  }
  .card--front .identity { top: 202px; color: var(--paper-text); }
  .card--back  .identity { top: 36px; right: 47px; color: var(--ink); }

  .identity__name {
    font-family: "Mrs Saint Delafield", cursive;
    font-size: 58px;
    line-height: 1;
    font-weight: 400;
    white-space: nowrap;
  }
  .identity__role {
    font-family: "Mulish", sans-serif;
    font-size: 11.5px;
    letter-spacing: 6px;
    margin-right: -6px;
    margin-top: 2px;
    font-weight: 500;
  }
  .card--back .identity__role {
    color: var(--sage);
    font-weight: 700;
    font-size: 11px;
    letter-spacing: 4px;
    margin-right: -4px;
    margin-top: -8px;
  }

  .contact {
    position: absolute;
    right: 50px;
    text-align: right;
    font-family: "Mulish", sans-serif;
    font-style: normal;
    font-weight: 700;
    font-size: 15.5px;
    line-height: 22.5px;
    letter-spacing: 1.8px;
    color: var(--ink);
  }
  .contact--reach { top: 134px; }
  .contact--address { top: 210px; right: 47px; }
</style>
</head>
<body>
  <main class="sheet">
    <section class="card card--front">
      <div class="card__photo" role="img" aria-label="Naturfoto: dunkelgrüne Farnwedel vor schwarzem Hintergrund"></div>
      <div class="identity">
        <p class="identity__name">Nachname Vorname</p>
        <p class="identity__role">TRAUERREDNERIN</p>
      </div>
    </section>

    <section class="card card--back">
      <div class="card__pattern" role="img" aria-label="Dezentes Blattmuster in hellem Salbeigrün"></div>
      <div class="identity">
        <p class="identity__name">Nachname Vorname</p>
        <p class="identity__role">TRAUERREDNERIN</p>
      </div>
      <address class="contact contact--reach">
        <p>+49170 55508642</p>
        <p>kontakt@mailpost.de</p>
      </address>
      <address class="contact contact--address">
        <p>Haus am Lindenhof</p>
        <p>N°7 Ahornallee</p>
        <p>20500 Stadt</p>
      </address>
    </section>
  </main>
</body>
</html>
```